【依頼目的】
佐世保市の新たな祭りのポスターを作成お願いしたい。

【イベント事業概要】
・来場者の方や、関係諸団体の方が本事業を通して佐世保の魅力を再認識し、さらに新しい魅力を発見してもらうことを目的とします。
・すべての来場者を市内周遊や宿泊等に結び付け、佐世保の賑わいを発信し、佐世保に訪れたいという気持ちを醸成することで来訪、再来訪につなげることを目的とします。
・若者が明るい未来を描くことができ、子育て世代が子供を産み、育てたいと思えるまち、そしてすべての人が生涯を過したいまちになる仕組みを創出することを目的とします。
・認知度が高い汐見バーガー等の観光資源のPRと旧軍港4都市のグルメイベント、また佐世保の新しい観光資源の発見とPRに尽力します。
・メインはフードですが、その他、アーティストライブ、スカイランタン、縁日等も複合した祭りです。

【依頼内容】
・新しいイベントであり、翌年以降も引き継ぐイベントである。
・官民連携による企画
・おしゃれな祭りにしたい希望であるが、行政も連携し、全年齢を対象としたイベントなの    で若向きになりすぎないよう多少の配慮必要

写真はあくまでイメージです。
また、イベント内容は変更になる可能性があるので写真等の枠を作っていただき変更できるような形が望ましいかもしれません。

全体のバランスと色合い等を評価されていました。

この度は、当コンペに多数の応募をいただき大変、ありがとうございました。
最終的には多数決で公平に審査いたしましたが
残念ながら当選されなかったかたには深くお詫び申し上げます。
私も仕事でよくモノタクトを利用していますので、またの機会があればよろしくお願い申し上げます。

```html
<!DOCTYPE html>
<html lang="ja">
<head>
<meta charset="utf-8">
<title>2022 MINATO FUN FESTIVAL</title>
<link href="https://fonts.googleapis.com/css2?family=Alfa+Slab+One&family=Dela+Gothic+One&family=M+PLUS+Rounded+1c:wght@500;800&family=Noto+Sans+JP:wght@400;700;900&family=Pacifico&display=swap" rel="stylesheet">
<style>
  :root{
    --yellow:#f6cf1a;
    --yellow-soft:#fbe36a;
    --cream:#fffdf3;
    --ink:#1d1d1d;
    --red:#c42a2a;
    --white:#ffffff;
  }
  *{box-sizing:border-box;margin:0;padding:0}
  html,body{width:849px;height:1200px;overflow:hidden;background:var(--cream)}
  .poster{position:relative;width:849px;height:1200px;overflow:hidden;background:var(--cream);font-family:"Noto Sans JP",sans-serif;color:var(--ink)}
  .dot{position:absolute;border-radius:50%;background:var(--yellow)}
  .photo{position:absolute;overflow:hidden}
  .photo--burger{left:0;top:0;width:250px;height:225px;border-radius:0 0 120px 0;background:linear-gradient(160deg,#6b3a1c,#b0702c 45%,#e3b25a 80%)}
  .photo--lantern{right:0;top:0;width:250px;height:260px;border-radius:0 0 0 130px;background:radial-gradient(circle at 40% 40%,#f0a040,#8a3a1c 55%,#2a1a20)}
  .photo--dance{left:-20px;top:365px;width:245px;height:160px;border-radius:0 80px 80px 0;background:linear-gradient(135deg,#f1f1ee,#cfcac2 60%,#8a857d)}
  .photo--mascot{left:-10px;top:640px;width:270px;height:150px;border-radius:0 75px 0 0;background:linear-gradient(180deg,#9bc2e2,#d9c6a8 60%,#b48a5c)}
  .photo--stage{right:0;top:425px;width:240px;height:155px;border-radius:80px 0 0 80px;background:linear-gradient(180deg,#a9c8e4,#c7c2b2 55%,#5d5c4c)}
  .photo--dome{right:0;top:600px;width:215px;height:150px;border-radius:75px 0 0 0;background:linear-gradient(180deg,#8fb3d6,#6d7d88 55%,#39484e)}
  .bubble{position:absolute;border-radius:50%;background:var(--white);display:flex;align-items:center;justify-content:center;text-align:center;font-family:"M PLUS Rounded 1c",sans-serif;font-weight:800;font-size:14px;line-height:1.35;box-shadow:0 0 0 3px var(--yellow)}
  .bubble--gourmet{left:20px;top:225px;width:120px;height:120px}
  .bubble--wish{left:665px;top:15px;width:120px;height:120px}
  .bubble--show{left:690px;top:290px;width:125px;height:125px}
  .headline{position:absolute;left:0;right:0;top:92px;text-align:center;font-family:"Noto Sans JP",sans-serif;font-weight:900;color:var(--ink)}
  .headline__year{font-size:38px;line-height:1.1;letter-spacing:2px}
  .headline__word{line-height:1}
  .headline__word--first{font-size:84px;letter-spacing:4px;margin-top:10px}
  .headline__word--second{font-size:94px;letter-spacing:48px;margin-right:-48px;margin-top:30px}
  .headline__word--festival{font-size:84px;letter-spacing:3px;margin-top:30px}
  .tagline{position:absolute;left:235px;top:494px;width:380px;height:46px;background:var(--yellow);border-radius:4px;display:flex;align-items:center;justify-content:center;font-family:"Dela Gothic One",sans-serif;font-size:25px;color:var(--white);letter-spacing:2px}
  .tagline em{font-style:normal;color:var(--red)}
  .date{position:absolute;left:0;right:0;top:575px;display:flex;justify-content:center;align-items:baseline;gap:10px;font-family:"Alfa Slab One",serif;color:var(--red)}
  .date__num{font-size:74px;line-height:1}
  .date__day{font-family:"M PLUS Rounded 1c",sans-serif;font-weight:800;font-size:18px;color:var(--white);background:var(--ink);border-radius:50%;width:44px;height:44px;display:inline-flex;align-items:center;justify-content:center;transform:translateY(-10px)}
  .date__day--sun{background:var(--red)}
  .hours{position:absolute;left:0;right:0;top:660px;text-align:center;font-family:"Alfa Slab One",serif;font-size:30px;letter-spacing:1px}
  .venue{position:absolute;left:0;right:0;top:704px;text-align:center;font-weight:700;font-size:19px;letter-spacing:2px}
  .city{position:absolute;left:0;top:745px;width:849px;height:420px;background:linear-gradient(180deg,#b9d3e8 0%,#8fb2cf 30%,#6f8f74 60%,#4f6b52 100%)}
  .pickup{position:absolute;left:22px;top:780px;font-family:"Pacifico",cursive;font-size:30px;color:var(--red);transform:rotate(-8deg)}
  .pickup-note{position:absolute;left:200px;top:798px;padding:6px 18px;background:var(--white);font-weight:700;font-size:16px;border-radius:3px}
  .event{position:absolute;display:flex;gap:10px}
  .event__photo{flex:none;background:linear-gradient(160deg,#7b451f,#c98a3c 55%,#e9c274)}
  .event__photo--lantern{background:radial-gradient(circle at 50% 45%,#f3a544,#7a2f1a 60%,#241417)}
  .event__body{display:flex;flex-direction:column;gap:6px}
  .event__label{background:var(--red);color:var(--white);font-weight:900;font-size:17px;padding:5px 8px;border-radius:2px;white-space:nowrap}
  .event__text{background:rgba(255,255,255,.92);font-size:12px;line-height:1.5;padding:6px 8px;flex:1}
  .event--burger{left:38px;width:385px}
  .event--burger .event__photo{width:125px;height:125px;border-radius:6px}
  .event--burger .event__body{flex:1}
  .event--row1{top:850px}
  .event--row2{top:1005px}
  .event--lantern{width:196px;flex-direction:column;gap:6px}
  .event--lantern .event__top{display:flex;gap:6px;align-items:flex-start}
  .event--lantern .event__photo{width:90px;height:90px;border-radius:4px}
  .event--lantern .event__label{font-size:12px;padding:4px 6px}
  .event--lantern .event__text{font-size:11px;height:46px}
  .col-a{left:438px}
  .col-b{left:640px}
  .footer{position:absolute;left:0;bottom:0;width:849px;height:38px;background:var(--white);display:flex;align-items:center;justify-content:center;gap:40px;font-size:14px;font-weight:700}
</style>
</head>
<body>
<main class="poster">
  <div class="dot" style="left:205px;top:-20px;width:70px;height:70px"></div>
  <div class="dot" style="left:570px;top:200px;width:50px;height:50px"></div>
  <div class="dot" style="left:130px;top:330px;width:55px;height:55px"></div>
  <div class="dot" style="left:590px;top:395px;width:38px;height:38px;background:var(--yellow-soft)"></div>
  <div class="dot" style="left:175px;top:560px;width:44px;height:44px;background:var(--yellow-soft)"></div>
  <div class="dot" style="left:780px;top:560px;width:60px;height:60px"></div>
  <div class="dot" style="left:220px;top:700px;width:40px;height:40px"></div>

  <div class="photo photo--burger" role="img" aria-label="ハンバーガーの写真"></div>
  <div class="photo photo--lantern" role="img" aria-label="夜空に浮かぶスカイランタンの写真"></div>
  <div class="photo photo--dance" role="img" aria-label="書の演舞のステージ写真"></div>
  <div class="photo photo--mascot" role="img" aria-label="会場の来場者の写真"></div>
  <div class="photo photo--stage" role="img" aria-label="屋外ステージのパフォーマンス写真"></div>
  <div class="photo photo--dome" role="img" aria-label="ドーム型テントの会場写真"></div>

  <div class="bubble bubble--gourmet">佐世保の<br>グルメを<br>味わいつくせ!</div>
  <div class="bubble bubble--wish">みんなで<br>一斉の<br>願い事タイム</div>
  <div class="bubble bubble--show">圧巻の<br>パフォーマンス!</div>

  <header class="headline">
    <div class="headline__year">2022</div>
    <div class="headline__word headline__word--first">MINATO</div>
    <div class="headline__word headline__word--second">FUN</div>
    <div class="headline__word headline__word--festival">FESTIVAL</div>
  </header>

  <div class="tagline">食と楽がつまった<em>2Days</em></div>

  <div class="date">
    <span class="date__num">4/4</span><span class="date__day">Sat</span>
    <span class="date__num">5</span><span class="date__day date__day--sun">Sun</span>
  </div>
  <div class="hours">Start-10:00 End-20:00</div>
  <div class="venue">会場：○○○○○○○○</div>

  <section class="city" role="img" aria-label="港町の街並みと海を見渡す風景写真"></section>

  <div class="pickup">Event Pick up!</div>
  <div class="pickup-note">注目のイベントをピックアップしてご紹介!</div>

  <article class="event event--burger event--row1">
    <div class="event__photo" role="img" aria-label="バーガーの写真"></div>
    <div class="event__body">
      <div class="event__label">バーガースタンプラリー</div>
      <p class="event__text">市内のバーガー店をめぐってスタンプを集めよう。全店制覇で特製グッズをプレゼント。</p>
    </div>
  </article>
  <article class="event event--burger event--row2">
    <div class="event__photo" role="img" aria-label="バーガーの写真"></div>
    <div class="event__body">
      <div class="event__label">バーガースタンプラリー</div>
      <p class="event__text">会場限定メニューも登場。食べ比べを楽しみながらお気に入りの一品を見つけよう。</p>
    </div>
  </article>

  <article class="event event--lantern event--row1 col-a">
    <div class="event__top">
      <div class="event__photo event__photo--lantern" role="img" aria-label="スカイランタンの写真"></div>
      <div class="event__label">スカイランタン</div>
    </div>
    <p class="event__text">夜空に願いを込めたランタンを一斉に放ちます。</p>
  </article>
  <article class="event event--lantern event--row1 col-b">
    <div class="event__top">
      <div class="event__photo event__photo--lantern" role="img" aria-label="スカイランタンの写真"></div>
      <div class="event__label">スカイランタン</div>
    </div>
    <p class="event__text">幻想的な光景をご家族で楽しめます。</p>
  </article>
  <article class="event event--lantern event--row2 col-a">
    <div class="event__top">
      <div class="event__photo event__photo--lantern" role="img" aria-label="スカイランタンの写真"></div>
      <div class="event__label">スカイランタン</div>
    </div>
    <p class="event__text">参加受付は会場本部テントにて行います。</p>
  </article>
  <article class="event event--lantern event--row2 col-b">
    <div class="event__top">
      <div class="event__photo event__photo--lantern" role="img" aria-label="スカイランタンの写真"></div>
      <div class="event__label">スカイランタン</div>
    </div>
    <p class="event__text">雨天時は内容を変更して実施します。</p>
  </article>

  <footer class="footer">
    <span>主催：MINATOFUNFESTIVAL 実行委員会</span>
    <span>お問い合わせ Tel.00-0000-0000　xxxxxx@mail.com</span>
  </footer>
</main>
</body>
</html>
```